Need Primer (paint) Label Design

THE ATTACHED LABEL/S ARE SOLEY FOR REFERENCE. DO NOT MAKE ME AN INTERIOR PAINT OR CHALK PAINT LABEL. I ONLY NEED A "PRIMER" LABEL. THE ATTACHED INTERIOR PAINT LABEL IS ONLY TO SHOW YOU THE THEME/DESIGN OF OUR OTHER LABELS. THE BLUE LABEL ONLY HAS A DESIGN ASPECT I LIKE (PRIMER ON SIDE). The last four labels are our competitors.
```````````````````````````````````````````````````````````````````````````````````````````````````
We need this label to look professional, sharp, eye catching and modern.
OUR PRIMARY COLORS ARE BLACK AND WHITE. IF YOU INCOPORATE ANOTHER COLOR, SILVER OR GOLD MIGHT BE IDEAL BUT PLEASE DON'T DRIFT TOO FAR.
The attached documents:
1st - Our Logo
2nd - Our chalk paint label (reference). We do not need a chalk paint label.
3rd. A random design example. I like the PRIME on the side running vertically. I think it's a cool design concept.
````````````````````````````````````````````````````````````````````````````````````````````````````
We are going to be using a normal paint can with a metal bail/handle so please use that with you design work
``````````````````````````````````````````````````````````````````````````````````````````````````
Order, in my head:
4327
Coatings
^^ I want this to stand out as well but I don't want it to be the first thing your eye is drawn to. Probably 2nd
Interior/Exterior
Multi - Surface Primer
^^ Want this to stick out and draw your eye so the customer knows what it is immediately
Exceptional Adhesion, Performance, Durability,
Use on Wood, Drywall, Plaster, Stucco, Masonry, Brick, Paneling, Painted Metal, & Properly Prepared Glossy Surfaces & More
35* Lowe Temperature Application (can be on side or small)
100% Acrylic
Low Odor - Low VOC - Soap & Water Clean Up
1 US Gallon - 3.785 L
Feel free to get creative with it!

```html
<!DOCTYPE html>
<html lang="en">
<head>
<meta charset="utf-8">
<title>4327 Coatings – Multi-Surface Primer Label</title>
<link rel="stylesheet" href="https://fonts.googleapis.com/css2?family=Open+Sans:wdth,wght@75..100,300..800&family=Permanent+Marker&display=swap">
<style>
  :root {
    --backdrop: #b4b2ab;
    --ink: #0b0b0b;
    --paper: #ffffff;
    --silver-dark: #6f6a66;
    --silver-mid: #a9a39e;
    --silver-light: #e6e2de;
    --band-text: #3a3735;
    --wall-light: #f1f2ee;
    --wall-shade: #d9dad5;
    --siding-light: #eef1f3;
    --siding-shade: #c9cfd4;
    --wood: #e3c79a;
  }
  * { margin: 0; padding: 0; box-sizing: border-box; }
  html, body {
    width: 1110px;
    height: 1200px;
    overflow: hidden;
  }
  body {
    background: radial-gradient(ellipse at 50% 45%, #c2c0ba 0%, var(--backdrop) 70%);
    font-family: "Open Sans", Arial, sans-serif;
    position: relative;
  }
  .brand-mark {
    position: absolute;
    left: 54px;
    top: 30px;
    color: var(--ink);
    font-family: "Open Sans", Arial, sans-serif;
    font-weight: 400;
    line-height: 1;
  }
  .brand-mark .brand-number {
    display: block;
    font-size: 112px;
    letter-spacing: -2px;
  }
  .brand-mark .brand-word {
    display: block;
    font-size: 27px;
    letter-spacing: 9px;
    margin-top: 6px;
    padding-left: 4px;
  }
  .primer-label {
    position: absolute;
    left: 55px;
    top: 470px;
    width: 1000px;
    height: 345px;
    box-shadow: 0 10px 30px rgba(0,0,0,0.18);
  }
  .primer-label svg { display: block; width: 100%; height: 100%; }
  .label-text { font-family: "Open Sans", Arial, sans-serif; font-stretch: 80%; }
  .prime-side { font-family: "Permanent Marker", "Open Sans", sans-serif; }
</style>
</head>
<body>

  <div class="brand-mark" aria-label="4327 Coatings">
    <span class="brand-number">4327</span>
    <span class="brand-word">COATINGS</span>
  </div>

  <div class="primer-label">
    <svg viewBox="0 0 1488 513" xmlns="http://www.w3.org/2000/svg">
      <defs>
        <linearGradient id="wallFill" x1="0" y1="0" x2="1" y2="1">
          <stop offset="0" stop-color="var(--wall-shade)"/>
          <stop offset="0.55" stop-color="var(--wall-light)"/>
          <stop offset="1" stop-color="var(--paper)"/>
        </linearGradient>
        <linearGradient id="sidingFill" x1="0" y1="0" x2="1" y2="1">
          <stop offset="0" stop-color="var(--siding-shade)"/>
          <stop offset="0.5" stop-color="var(--siding-light)"/>
          <stop offset="0.8" stop-color="var(--siding-light)"/>
          <stop offset="1" stop-color="var(--wood)"/>
        </linearGradient>
        <linearGradient id="silverBand" x1="0" y1="0" x2="1" y2="0">
          <stop offset="0" stop-color="var(--silver-dark)"/>
          <stop offset="0.45" stop-color="var(--silver-light)"/>
          <stop offset="0.6" stop-color="var(--silver-mid)"/>
          <stop offset="1" stop-color="var(--silver-dark)"/>
        </linearGradient>
      </defs>

      <rect class="photo-roller" x="0" y="0" width="745" height="320" fill="url(#wallFill)"
            role="img" aria-label="Photo of a paint roller applying white primer to a wall"/>
      <rect class="photo-brush" x="745" y="0" width="743" height="320" fill="url(#sidingFill)"
            role="img" aria-label="Photo of a brush priming white siding boards over bare wood"/>

      <path class="silver-band" d="M0,200 Q744,320 1488,185 L1488,195 Q744,390 0,215 Z" fill="url(#silverBand)"/>
      <path class="black-base" d="M0,215 Q744,390 1488,195 L1488,513 L0,513 Z" fill="var(--ink)"/>

      <rect class="logo-panel" x="577" y="58" width="333" height="208" fill="var(--ink)"/>
      <text class="label-text" x="743" y="182" text-anchor="middle" fill="var(--paper)" font-size="132" font-weight="400" style="font-stretch:100%">4327</text>
      <text class="label-text" x="746" y="236" text-anchor="middle" fill="var(--paper)" font-size="38" font-weight="400" letter-spacing="9" style="font-stretch:100%">COATINGS</text>

      <text class="label-text" x="743" y="291" text-anchor="middle" fill="var(--band-text)" font-size="27" font-weight="500" letter-spacing="1">INTERIOR | EXTERIOR</text>

      <text class="label-text" x="743" y="333" text-anchor="middle" fill="var(--paper)" font-size="31" font-weight="700">MULTI - SURFACE PRIMER</text>

      <rect x="662" y="345" width="164" height="27" fill="none" stroke="var(--paper)" stroke-width="1.5"/>
      <text class="label-text" x="744" y="366" text-anchor="middle" fill="var(--paper)" font-size="19" font-weight="700">100% ACRYLIC</text>

      <text class="label-text" x="743" y="393" text-anchor="middle" fill="var(--paper)" font-size="14" font-weight="600">EXCEPTIONAL ADHESION | PERFORMANCE | DURABILITY</text>

      <text class="label-text" x="743" y="411" text-anchor="middle" fill="var(--paper)" font-size="9.5" font-weight="400">Use on Wood | Drywall | Plaster | Stucco | Masonry | Brick</text>
      <text class="label-text" x="743" y="422" text-anchor="middle" fill="var(--paper)" font-size="9.5" font-weight="400">Paneling | Painted Metal | &amp; Properly Prepared Glossy Surfaces &amp; More</text>

      <line x1="602" y1="433" x2="692" y2="433" stroke="var(--paper)" stroke-width="1"/>
      <line x1="796" y1="433" x2="886" y2="433" stroke="var(--paper)" stroke-width="1"/>
      <text class="label-text" x="744" y="436" text-anchor="middle" fill="var(--paper)" font-size="6.5" font-weight="400">35° Low Temperature Application</text>

      <text class="label-text" x="743" y="454" text-anchor="middle" fill="var(--paper)" font-size="13" font-weight="500">Low Odor - Low VOC - Soap &amp; Water Clean Up</text>

      <text class="label-text" x="743" y="477" text-anchor="middle" fill="var(--paper)" font-size="11" font-weight="600">1 US Gallon 3.785 L</text>

      <text class="prime-side" x="0" y="0" transform="translate(1003,290) rotate(-90)" text-anchor="middle" fill="var(--paper)" font-size="92">PRIME</text>
    </svg>
  </div>

</body>
</html>
```